Marketing - Outdoor Vinyl banner, Outdoor Poster, Flyer modifications

Hi, I worked with you in the past and attached flyer designs. It just needs to be tweaked for various prints.
1)Outdoor vinyl banner (4 feet height and 8 feet width) print: Just grand opening pic, logo with name, tagline and call/text us portion.
2)Outdoor Poster (5 feet height and 3 feet width) print: same as above
3) Indoor poster for both horizontal & Vertical prints: Just logo w/ name, tagline, "We are MOVING Next door"
4)Flyer: will give minor modifications to attached flyer designs

```html
<!DOCTYPE html>
<html lang="en">
<head>
<meta charset="UTF-8">
<title>Brightway Dentistry – We're Moving Next Door</title>
<link href="https://fonts.googleapis.com/css2?family=Playfair+Display:wght@400;700;900&display=swap" rel="stylesheet">
<style>
  :root {
    --sky: #0cb1da;
    --slate: #627c98;
    --white: #ffffff;
    --page: #ffffff;
  }
  * { margin: 0; padding: 0; box-sizing: border-box; }
  html, body {
    width: 1200px;
    height: 1200px;
    overflow: hidden;
    background: var(--page);
  }
  .poster {
    position: absolute;
    left: 289px;
    top: 89px;
    width: 629px;
    height: 1029px;
    background: var(--white);
    box-shadow: 0 0 18px rgba(60, 80, 110, 0.35);
    overflow: hidden;
    font-family: "Playfair Display", serif;
  }
  .poster-shapes {
    position: absolute;
    inset: 0;
    width: 629px;
    height: 1029px;
  }
  .brand {
    position: absolute;
    top: 83px;
    left: 0;
    width: 629px;
    display: flex;
    align-items: center;
    justify-content: center;
    gap: 14px;
  }
  .brand-dot {
    width: 44px;
    height: 44px;
    border-radius: 50%;
    background: var(--sky);
  }
  .brand-name {
    color: var(--sky);
    font-weight: 700;
    font-size: 34px;
    letter-spacing: 1px;
    line-height: 1;
  }
  .headline {
    position: absolute;
    left: 0;
    width: 629px;
    text-align: center;
    color: var(--white);
    line-height: 1;
    white-space: nowrap;
  }
  .headline-intro {
    top: 348px;
    font-size: 70px;
    font-weight: 400;
  }
  .headline-next {
    top: 439px;
    font-size: 176px;
    font-weight: 900;
    letter-spacing: -3px;
  }
  .headline-door {
    top: 590px;
    font-size: 176px;
    font-weight: 900;
    letter-spacing: -9px;
  }
  .tagline {
    position: absolute;
    left: 0;
    top: 948px;
    width: 629px;
    text-align: center;
    color: var(--white);
    font-size: 40px;
    font-weight: 700;
    line-height: 1;
    white-space: nowrap;
  }
</style>
</head>
<body>
  <div class="poster">
    <svg class="poster-shapes" viewBox="0 0 629 1029" aria-hidden="true">
      <path fill="var(--slate)" d="M0,204 C40,240 80,245 120,243 C220,235 320,170 445,170 C330,175 220,262 120,272 C80,276 40,262 0,228 Z"/>
      <path fill="var(--sky)" stroke="var(--white)" stroke-width="2" d="M0,232 C40,270 80,280 120,275 C220,262 320,175 420,173 C500,172 570,200 629,231 V1029 H0 Z"/>
      <path fill="var(--white)" d="M9,1029 C80,880 200,820 313,820 C430,820 550,890 616,1029 Z"/>
      <path fill="var(--slate)" d="M15,1029 C90,900 200,851 313,851 C430,851 540,900 610,1029 Z"/>
    </svg>

    <div class="brand">
      <span class="brand-dot"></span>
      <span class="brand-name">BRIGHTWAY DENTISTRY</span>
    </div>

    <h1 class="headline headline-intro">We’re MOVING</h1>
    <p class="headline headline-next">Next</p>
    <p class="headline headline-door">DOOR!</p>

    <p class="tagline">Exciteed to find home!</p>
  </div>
</body>
</html>
```